brolvin business card design so that it looks better

need a new business card designed. use our website, brolvix.example for example. I attached an example of a previous card we had and liked. this is for law enforcement and we have attached a previous business card as an example. This site forces me to select color and font, ignore those as I picked stuff just to get this completed.

Target Market(s)

law enforcement, local government

Contact Information for Business Card

see the attached example and our website

Font styles to use
Serif

```html
<!DOCTYPE html>
<html lang="en">
<head>
<meta charset="utf-8">
<title>Brolvin Business Card</title>
<link rel="stylesheet" href="https://fonts.googleapis.com/css2?family=Lato:wght@300;400;700&display=swap">
<style>
  :root {
    --backdrop: #d9d9d9;
    --card-white: #ffffff;
    --navy: #041a26;
    --ink: #0d1c26;
    --ink-soft: #2a3740;
    --rule: #d4d8db;
    --on-navy: #ffffff;
  }
  * { box-sizing: border-box; margin: 0; padding: 0; }
  html, body { width: 1200px; height: 802px; overflow: hidden; }
  body {
    background: var(--backdrop);
    font-family: "Lato", sans-serif;
    position: relative;
  }
  .card {
    position: absolute;
    top: 274px;
    width: 443px;
    height: 265px;
    box-shadow: 2px 3px 6px rgba(0,0,0,0.35);
  }
  .card-front { left: 136px; background: var(--card-white); }
  .card-back { left: 624px; background: var(--navy); }

  .brand-name {
    position: absolute;
    font-family: "Lato", sans-serif;
    font-weight: 300;
    letter-spacing: 4px;
    white-space: nowrap;
  }
  .card-front .brand-name {
    left: 0; width: 220px; top: 118px;
    text-align: center;
    font-size: 30px;
    color: var(--ink);
  }
  .divider {
    position: absolute;
    left: 220px; top: 66px;
    width: 1px; height: 140px;
    background: var(--rule);
  }
  .contact {
    position: absolute;
    left: 245px; top: 72px;
    color: var(--ink-soft);
    font-size: 12.5px;
    line-height: 16px;
  }
  .person-name {
    font-weight: 700;
    font-size: 14.5px;
    letter-spacing: 0.5px;
    color: var(--ink);
    line-height: 17px;
  }
  .person-role { margin-bottom: 6px; }
  .contact-line { display: flex; align-items: center; gap: 5px; }
  .contact-line svg { width: 9px; height: 9px; fill: var(--ink); flex: none; }
  .address { margin-top: 5px; padding-left: 2px; }

  .service-band {
    position: absolute;
    left: 0; bottom: 0;
    width: 100%; height: 41px;
    background: var(--navy);
    color: var(--on-navy);
    font-size: 12.5px;
    display: flex; align-items: center; justify-content: center;
    gap: 6px;
  }
  .service-band .dot {
    width: 5px; height: 5px; border-radius: 50%;
    background: var(--on-navy);
    display: inline-block;
  }

  .card-back .brand-name {
    left: 0; width: 100%; top: 108px;
    text-align: center;
    font-size: 40px;
    color: var(--on-navy);
  }
  .tagline {
    position: absolute;
    left: 0; width: 100%; top: 168px;
    text-align: center;
    color: var(--on-navy);
    font-size: 12.5px;
    letter-spacing: 0.4px;
  }
</style>
</head>
<body>
  <section class="card card-front">
    <div class="brand-name">BROLVIN</div>
    <div class="divider"></div>
    <div class="contact">
      <div class="person-name">MARCUS HALE</div>
      <div class="person-role">Managing Director</div>
      <div class="contact-line">
        <svg viewBox="0 0 10 10"><path d="M1 3c0-1 1-2 4-2s4 1 4 2v1H7V3H3v1H1zM2 5h6l1 4H1z"/></svg>
        <span>555.014.2290</span>
      </div>
      <div class="contact-line">
        <svg viewBox="0 0 10 10"><path d="M0 2h10v6H0z M0 2l5 3.5L10 2" fill="none" stroke="currentColor" stroke-width="0"/><rect x="0" y="2" width="10" height="6"/><path d="M0.5 2.5l4.5 3 4.5-3" stroke="#fff" stroke-width="0.9" fill="none"/></svg>
        <span>info@brolvix.example</span>
      </div>
      <div class="contact-line">
        <svg viewBox="0 0 10 10"><circle cx="5" cy="5" r="4.5"/><path d="M0.5 5h9M5 0.5c-2 2-2 7 0 9M5 0.5c2 2 2 7 0 9" stroke="#fff" stroke-width="0.7" fill="none"/></svg>
        <span>www.brolvix.example</span>
      </div>
      <div class="address">4120 Larkspur Avenue<br>Fairview, TX 75000</div>
    </div>
    <div class="service-band">
      <span>Law Enforcement</span><span class="dot"></span>
      <span>Justice of the Peace</span><span class="dot"></span>
      <span>Municipal Courts</span>
    </div>
  </section>

  <section class="card card-back">
    <div class="brand-name">BROLVIN</div>
    <div class="tagline">LAW ENFORCEMENT INNOVATION</div>
  </section>
</body>
</html>
```